Lively Ledgers - Minimalistic Single Page Web Design

Project: We are in the process of creating a new Corp Identity. Design a website for our company incorporating the Logo recently designed and selected from a ArtMarketo contest. (attached)

Designers: For this project, you need to design a minimalistic single page, modern website. Beside text and image placement, you will also need to describe user interface, how content is presented and so on.
- Design Layout
- Design Image placements (if any)
- Design menu and buttons
- Design menu and buttons placements
- Design content layout
- Design overall effect and feel of website
- Design color scheme
- Design content style (tone and style of content, words type, how much)
- Design user interface (how do you scroll, what happens when you mouseover buttons, where do certain links and buttons lead you)

Coding Requirements: You need to design the website with a modern perspective on website visuals and effects. Jquery, HTML5 (no FLASH please). You do not need to code for this particular contest, but if you can also code, great, tell me and let me know how I can hire you to complete it. If you know someone that can code your vision, great, let me know. If not, you need to be clear and concise, and be willing to help me communicate with a developer to get the site executed. The web site needs to be modern and dynamic.

Company Name:
Lively Ledgers; Lively-Ledgers; LivelyLedgers

Domain: www.lively-ledgers.com

Company Industry:
Lively Ledgers provides consulting in areas of finance, accounting, business organization, and set up.
- Bookkeeping
- Project Management
- Budget Management
- Cash Management
- Receipt Management
- Filing and Records Management
- Training of administration and accounting staff
- Financial Reports
- Spreadsheets
- Graphs, charts and trend analysis
- Business set up
- Tax filings
- Payroll and HR

Clients:
- Small to medium size businesses
- Proprietors
- Entrepreneurs
- Mom & Pops Shops
- We cater to every industry

Corporate Identity:
- Past: I have never complete a webpage for my company. I did scratch several projects that were started and never completed. I fell in love with stick figures, whimsical designs, similar to that of "Cloudvat", I believed in simplicity and minimalism. However, I was not effective in find the right people to complete my project. Bits and pieces of the website was designed, but never executed.

- Current: I need a webpage design. The web design must align with the current logo aesthetics.The current logo is new. I selected this logo for its simplicity and modern feel. It also incorporated an image of a trending graph, which fits with my company's profile. Still, I am leaning towards simple design, minimalism with boldness. I like my new webpage to be mature and professional, but I want it to portray energy and youth. So no "traditional corp" like design. I like new HTML5 elements, jquery and fun and beautiful forms and buttons. Less image is more.

Note: Please improvise according to your taste and professional perspective, you do not have to follow my suggestions word for word.

Features & Layout:
- Single page layout
- Vertical scroll
- Framed sections so that it looks good on the screen
- Well designed and strategically placed menu bar
- Fills a modern browser
- Beautiful color scheme that pops
- Incorporate Logo aesthetics

Fonts and Type:
- This is an element of the overall design
- I love clean fonts
- Fonts that adds meaning to the overall effect
- Clean

Sounds
- Please no cheesy sounds and background music

Images:
- To your liking
- But please, no lame corp people in suits
- No lame photographs
- I like stick figures
- I like whimsical illustrations

Landing Page:
- This should be the bulk of your design
- The landing page must be impressive, eye catchy
- Bold

Menu Bar:
- Header (introduction and landing page)
- Service & Products
- Company (about us)
- Affiliates and Clients (reference area)
- Contact (contact us area)
- Footer

Colors:
- Up to you, I just like things clean and easy to read
- No black background behind text
- Incorporate Logo Colors

Web Effects:
- According to your liking
- You will need to be involve to communicate the layout and design to the developer, so you need to be clear in your design.

Content:
- You personally don't have to come up with the content, but if you can great.
- I will help come up with the content throughout the contect timeframe, just let me know what you want
- I do not like too much content in my website. The most for each section is 2-3 lines if any.
- Combination could also be one liners.
- I like minimalistic approach.
- If you are not creating the final content, you need to show what type of content need to be created and in what style or tone.

Samples and Inspirations:
- http://singlesheetgallery.example/
- http://vantorix.example/#top
- http://brightmopservices.example/#about
- http://layoutjournal.example/inspiration/23-inspiring-single-page-designs
- http://www.kelvarstudio.example/
- http://www.dariuskessley.example/

This I do not want:
- Too much popups (none if possible)
- Images of people
- Images of people in suits
- Stereotypical images of accountants
- Scrolling marquee
- Clip arts
Updates

Designers, I want to stress the fact that I am looking for a design, not simply a website. The website is 1 page long. Text and content should be minimal. So this means that the design has to do most of the talking. Please do not submit template like web designs, I can pull this off myself if needed. I need you to design a great header, footer and the connecting tissue from landing to end of the page. The entire design needs to flow.

Again, please do not use images of corp people or anything like that. Please think outside the box in how you want to express the company.

Some ideas:
An illustration from beginning to end of the website, have a story.
Add colors to the back ground. 
The background should not get in the way of reading the text, but it does not have to be boring.
Be bold in your design.

Also, please describe more about your design when you submit. Please don't submit a template like design and have no explanation for your actions.

Also, fee free to ask me questions. I am here to help. I check this everyday, so please contact if you need anything.

Designers, please read the details of my post before you submit the design.

If you have a great concept idea but is worry, you can go ahead and submit a pencil draft and ask my opinion before you work anymore on it.

Please see the website samples below for what I am really looking for:

Reason: Hi everyone, I am extending the deadline. It looks like some design are still pending completion, and I want you to have enough time to work on it.

```html
<!DOCTYPE html>
<html lang="en">
<head>
<meta charset="utf-8">
<title>Lively Ledgers</title>
<link rel="stylesheet" href="https://fonts.googleapis.com/css2?family=Comfortaa:wght@300;400&family=Quicksand:wght@400;500&display=swap">
<style>
:root{
  --lime:#8fc31f;
  --lime-bright:#9bd11e;
  --lime-dark:#5e8f0e;
  --ink:#555555;
  --ink-soft:#777777;
  --steel:#6f6f6f;
  --tile:#7a7a7a;
  --paper:#ffffff;
  --footer:#6b6b6b;
}
*{margin:0;padding:0;box-sizing:border-box}
html,body{width:1200px;height:2400px;overflow:hidden;background:var(--paper)}
body{position:relative;font-family:"Quicksand",sans-serif;color:var(--ink)}
.abs{position:absolute}

/* left backdrop */
.side-band{left:0;top:0;width:160px;height:2296px;
  background:linear-gradient(180deg,#a6d51f 0%,#8cc21a 40%,#7fb81a 70%,#9ccb2a 100%)}
.side-rule{left:160px;top:0;width:16px;height:2296px;background:var(--steel)}
.side-edge{left:176px;top:0;width:6px;height:2296px;background:var(--lime-bright)}

.side-words{left:200px;width:20px;font-family:"Comfortaa",sans-serif;font-size:11px;line-height:13px;
  color:var(--ink-soft);writing-mode:vertical-lr;text-orientation:upright;letter-spacing:0}

/* header */
.brand{left:206px;top:14px;font-family:"Comfortaa",sans-serif;font-weight:300;font-size:60px;color:var(--ink);letter-spacing:1px}
.brand-mark{left:196px;top:40px;width:22px;height:22px;background:var(--lime);border-radius:50%;display:none}
.main-nav{left:294px;top:148px;width:760px;font-family:"Comfortaa",sans-serif;font-size:17px;color:#444}
.main-nav a{position:absolute;color:inherit;text-decoration:none;white-space:nowrap}
.main-nav a.is-active{color:var(--lime)}
.hero{left:294px;top:196px;width:700px;height:350px;
  background:linear-gradient(160deg,#f2f2f2 0%,#dfe9cf 35%,#a9d35a 55%,#6fa82a 70%,#e8ece4 90%)}

/* section headings */
.section-title{left:204px;font-family:"Comfortaa",sans-serif;font-weight:400;font-size:60px;color:var(--lime);line-height:1;letter-spacing:-1px}

/* about */
.about-intro{left:290px;top:712px;width:660px;font-size:17px;line-height:22px;color:#444}
.service-cloud{left:290px;top:764px;width:640px;font-family:"Comfortaa",sans-serif;color:var(--ink-soft);z-index:2}
.service-cloud .row{height:29px;white-space:nowrap;font-size:21px;line-height:29px}
.service-cloud .key{color:var(--lime);font-size:30px;margin-right:14px}
.service-cloud .minor{margin-right:14px}
.growth-chart{left:292px;top:760px;width:706px;height:306px;z-index:1}

/* side tabs */
.side-tab{left:1020px;width:36px;background:var(--steel);border-radius:0 4px 4px 0;box-shadow:3px 4px 6px rgba(0,0,0,.35)}
.side-tab span{position:absolute;left:9px;top:8px;writing-mode:vertical-rl;font-size:15px;color:var(--lime-bright);white-space:nowrap;font-family:"Quicksand",sans-serif}
.tab-lead{left:950px;width:72px;height:6px;background:linear-gradient(90deg,rgba(111,111,111,0),var(--steel));border-radius:3px}

/* affiliates */
.client-tile{width:142px;height:140px;background:var(--tile);color:#b9b9b9;text-align:center;font-family:"Comfortaa",sans-serif}
.client-tile .label{display:block;margin-top:54px;font-size:13px}
.client-tile .name{display:block;font-size:15px}
.client-quote{left:472px;top:1224px;width:158px;height:156px;background:var(--lime-bright);color:#fff;padding:10px 12px;font-size:10px;line-height:12px;box-shadow:0 3px 6px rgba(0,0,0,.3)}
.client-quote .by{margin-top:18px;display:block}

/* products */
.product-art{left:296px;top:1694px;width:256px;height:266px;
  background:radial-gradient(circle at 70% 55%,#7fc41f 0%,#9fd34a 30%,#e6e6e6 60%,#ffffff 80%)}
.product-copy{left:568px;top:1744px;width:440px;font-size:17px;line-height:20px;color:#444}

/* contact */
.contact-card{left:292px;top:2100px;width:322px;height:196px;background:var(--lime-bright);padding:14px 24px;font-size:16px;line-height:19px;color:#4b5b2a}
.contact-form{left:682px;top:2100px;width:322px;height:196px;background:var(--lime-bright)}
.contact-form label{position:absolute;left:14px;font-size:16px;color:#4b5b2a}
.contact-form .field{position:absolute;left:88px;width:216px;height:26px;background:#fff;border:2px solid #d6ec9c}
.contact-form .message{position:absolute;left:12px;top:86px;width:292px;height:60px;background:#fff;border:2px solid #d6ec9c}
.contact-form .submit{position:absolute;left:250px;top:152px;font-size:16px;color:#4b5b2a}
.contact-form .submit-line{position:absolute;left:236px;top:172px}

/* footer */
.site-footer{left:0;top:2296px;width:1200px;height:104px;background:var(--footer);color:#fff;text-align:center;font-size:13px;line-height:16px;padding-top:30px}
</style>
</head>
<body>

<div class="abs side-band" role="img" aria-label="Green backdrop with faint spreadsheet figures and charts"></div>
<div class="abs side-rule"></div>
<div class="abs side-edge"></div>

<div class="abs side-words" style="top:92px">Welcome to livelyledgers What you need to know</div>
<div class="abs side-words" style="top:674px">can be probably discovered through our</div>
<div class="abs side-words" style="top:1180px">Our company offers a great variety of</div>
<div class="abs side-words" style="top:1672px">if you need to learn more just</div>

<header>
  <div class="abs brand">lively ledgers</div>
  <nav class="abs main-nav">
    <a style="left:0">about us</a>
    <a class="is-active" style="left:148px">service &amp; products</a>
    <a style="left:384px">affiliates &amp; clients</a>
    <a style="left:606px">contact us</a>
  </nav>
  <div class="abs hero" role="img" aria-label="Photo of a calculator, glasses, pen and green pie charts on a desk"></div>
</header>

<section>
  <h2 class="abs section-title" style="top:608px">about us</h2>
  <p class="abs about-intro">Lively Ledgers provides consulting in areas of finance, accounting, business organization, and set up.</p>
  <svg class="abs growth-chart" viewBox="0 0 706 306" aria-hidden="true">
    <defs>
      <linearGradient id="barFill" x1="0" y1="0" x2="1" y2="1">
        <stop offset="0" stop-color="#b5de4f"/><stop offset="0.6" stop-color="#7fb51c"/><stop offset="1" stop-color="#5c8c10"/>
      </linearGradient>
    </defs>
    <rect x="0" y="256" width="66" height="48" fill="url(#barFill)"/>
    <rect x="92" y="272" width="64" height="32" fill="url(#barFill)"/>
    <rect x="182" y="256" width="66" height="48" fill="url(#barFill)"/>
    <rect x="274" y="166" width="66" height="138" fill="url(#barFill)"/>
    <rect x="366" y="136" width="64" height="168" fill="url(#barFill)"/>
    <rect x="456" y="136" width="64" height="168" fill="url(#barFill)"/>
    <rect x="548" y="60" width="64" height="244" fill="url(#barFill)"/>
    <rect x="640" y="10" width="62" height="294" fill="url(#barFill)"/>
  </svg>
  <div class="abs service-cloud">
    <div class="row"><span class="key">Spreadsheets</span><span class="minor">Graphs, charts and trend analysis</span></div>
    <div class="row"><span class="minor">Business set up</span><span class="minor">Budget Management</span><span class="key">Bookkeeping</span></div>
    <div class="row"><span class="minor">Training of administration and accounting staff</span></div>
    <div class="row"><span class="minor">Filing and Records Management</span><span class="key">Tax filings</span></div>
    <div class="row"><span class="key">Payroll and HR</span><span class="minor">Cash Management</span></div>
    <div class="row"><span class="minor">Project Management</span></div>
    <div class="row"><span class="key">Financial Reports</span></div>
    <div class="row"><span class="minor">Receipt Management</span></div>
  </div>
  <div class="abs tab-lead" style="top:738px"></div>
  <div class="abs side-tab" style="top:736px;height:144px"><span>find out more</span></div>
</section>

<section>
  <h2 class="abs section-title" style="top:1110px">affiliates &amp; clients</h2>
  <div class="abs client-tile" style="left:292px;top:1232px"><span class="label">sample logo</span><span class="name">livelyledgers</span></div>
  <div class="abs client-quote">Lorem ipsum dolor sit amet, consectetur adipisicing elit, sed do eiusmod tempor incididunt ut labore et dolore magna aliqua. Ut enim ad minim veniam, quis nostrud exercitation ullamco laboris.<span class="by">Ella Marsh<br>General Manager</span></div>
  <div class="abs client-tile" style="left:668px;top:1232px"><span class="label">sample logo</span><span class="name">livelyledgers</span></div>
  <div class="abs client-tile" style="left:856px;top:1232px"><span class="label">sample logo</span><span class="name">livelyledgers</span></div>
  <div class="abs client-tile" style="left:292px;top:1414px"><span class="label">sample logo</span><span class="name">livelyledgers</span></div>
  <div class="abs client-tile" style="left:480px;top:1414px"><span class="label">sample logo</span><span class="name">livelyledgers</span></div>
  <div class="abs client-tile" style="left:668px;top:1414px"><span class="label">sample logo</span><span class="name">livelyledgers</span></div>
  <div class="abs client-tile" style="left:856px;top:1414px"><span class="label">sample logo</span><span class="name">livelyledgers</span></div>
  <div class="abs tab-lead" style="top:1196px"></div>
  <div class="abs side-tab" style="top:1194px;height:110px"><span>see more</span></div>
</section>

<section>
  <h2 class="abs section-title" style="top:1600px">products &amp; services</h2>
  <div class="abs product-art" role="img" aria-label="Illustration of a stick figure pointing at a rising green chart"></div>
  <p class="abs product-copy">Lorem ipsum dolor sit amet, consectetur adipisicing elit, sed do eiusmod tempor incididunt ut labore et dolore magna aliqua. Ut enim ad minim veniam, quis nostrud exercitation ullamco laboris nisi ut aliquip ex ea commodo consequat.<br>Lorem ipsum dolor sit amet, consectetur adipisicing elit, sed do eiusmod tempor incididunt ut labore et dolore magna aliqua. Ut enim ad minim veniam, quis nostrud exercitation ullamco laboris nisi ut aliquip ex ea commodo consequat.</p>
  <div class="abs tab-lead" style="top:1714px"></div>
  <div class="abs side-tab" style="top:1712px;height:110px"><span>learn more</span></div>
</section>

<section>
  <h2 class="abs section-title" style="top:2012px">contact us</h2>
  <address class="abs contact-card" style="font-style:normal">Lively Ledgers<br>xxxxxxxxxxxx street<br>xxxxxx City<br>State<br>telephone: xxxxxxxxxxxxxx</address>
  <form class="abs contact-form">
    <label style="top:12px">name</label><span class="field" style="top:14px"></span>
    <label style="top:46px">e-mail</label><span class="field" style="top:48px"></span>
    <span class="message"></span>
    <span class="submit">submit</span>
    <svg class="submit-line" width="70" height="10" viewBox="0 0 70 10" aria-hidden="true"><path d="M0 2 H70 L40 9 Z" fill="#6f6f6f"/></svg>
  </form>
</section>

<footer class="abs site-footer">Copyright © 2013 Lively Ledgers<br>All Rights Reserved<br>Terms of Use</footer>

</body>
</html>
```